Ward Compass Business Card Design*

We need a business card design for our company Ward Compass. Our company is specialized in providing online consulting services regarding medical institutions, hospitals and doctors. We work with patients worldwide looking to choose between healthcare providers. We have a website you may use as a reference, where we list doctors and clinics worldwide. So we target Medical providers as well as patients worldwide.
Target Market(s)
Medical Providers and patients around the world
Industry/Entity Type
Medical
Contact Information for Business Card
Salma Derkaoui
CEO
+90 612 348 2071
info@wardcompass-example.com
www.wardcompass-example.com
14 Annakhil 3 H.R.B. Rabat, Morocco
Requirements
Must have
- Company logo/name on one full side, personal info and smaller logo and company name on the other side.
Nice to have
- Smart and elegant design

```html
<!DOCTYPE html>
<html lang="en">
<head>
<meta charset="utf-8">
<title>Ward Compass Business Card</title>
<link rel="stylesheet" href="https://fonts.googleapis.com/css2?family=Montserrat:wght@300;400;600&display=swap">
<style>
  :root {
    --page: #e9eaec;
    --navy: #123b65;
    --grey-card: #7a7a7a;
    --white: #ffffff;
    --ink: #3a3a3a;
    --muted: #8a8a8a;
  }
  * { box-sizing: border-box; margin: 0; padding: 0; }
  html, body {
    width: 1200px; height: 960px; overflow: hidden;
    background: var(--page);
    font-family: "Montserrat", sans-serif;
  }
  .sheet {
    width: 1200px; height: 960px;
    display: flex; flex-direction: column; align-items: center; justify-content: center;
    gap: 36px;
  }
  .card {
    position: relative;
    width: 760px; height: 434px;
    box-shadow: 0 10px 28px rgba(0,0,0,.18);
    overflow: hidden;
  }
  /* Back side */
  .card-back { background: var(--grey-card); color: var(--white); }
  .back-brand {
    position: absolute; left: 0; right: 0; top: 150px;
    display: flex; align-items: center; justify-content: center; gap: 18px;
  }
  .back-brand .dot {
    width: 34px; height: 34px; border-radius: 50%; background: var(--white);
  }
  .back-brand .name {
    font-size: 40px; font-weight: 400; letter-spacing: 4px; text-transform: uppercase;
  }
  .back-url {
    position: absolute; left: 0; right: 0; bottom: 96px;
    text-align: center; font-size: 15px; font-weight: 400; letter-spacing: 4px;
  }
  /* Front side */
  .card-front { background: var(--white); }
  .front-band {
    position: absolute; left: 0; top: 0; bottom: 0; width: 180px;
    background: var(--navy);
  }
  .front-brand {
    position: absolute; left: 130px; top: 56px;
    display: flex; align-items: center; gap: 16px;
  }
  .front-brand .dot {
    width: 84px; height: 84px; border-radius: 50%;
    background: var(--white); border: 10px solid var(--navy);
  }
  .front-brand .name {
    font-size: 28px; font-weight: 600; color: var(--navy);
    letter-spacing: 1px; text-transform: uppercase;
  }
  .contact {
    position: absolute; right: 44px; top: 150px;
    text-align: right; color: var(--ink);
  }
  .contact .person { font-size: 30px; font-weight: 600; color: var(--navy); line-height: 1.1; }
  .contact .role { font-size: 15px; color: var(--muted); letter-spacing: 1px; margin-bottom: 14px; }
  .contact .line {
    display: flex; justify-content: flex-end; align-items: center; gap: 8px;
    font-size: 15px; line-height: 24px;
  }
  .contact .line svg { width: 13px; height: 13px; fill: var(--navy); flex: none; }
  .contact .line.address { padding-right: 21px; }
</style>
</head>
<body>
<main class="sheet">
  <section class="card card-back" aria-label="Card back">
    <div class="back-brand">
      <span class="dot"></span>
      <span class="name">Ward Compass</span>
    </div>
    <p class="back-url">www.wardcompass-example.com</p>
  </section>

  <section class="card card-front" aria-label="Card front">
    <div class="front-band"></div>
    <div class="front-brand">
      <span class="dot"></span>
      <span class="name">Ward Compass</span>
    </div>
    <div class="contact">
      <p class="person">Salma Derkaoui</p>
      <p class="role">CEO</p>
      <p class="line">+90 612 348 2071
        <svg viewBox="0 0 24 24" aria-hidden="true"><path d="M6.6 10.8a15.1 15.1 0 0 0 6.6 6.6l2.2-2.2a1 1 0 0 1 1-.25 11.4 11.4 0 0 0 3.6.57 1 1 0 0 1 1 1V20a1 1 0 0 1-1 1A17 17 0 0 1 3 4a1 1 0 0 1 1-1h3.5a1 1 0 0 1 1 1c0 1.25.2 2.45.57 3.57a1 1 0 0 1-.25 1z"/></svg></p>
      <p class="line">info@wardcompass-example.com
        <svg viewBox="0 0 24 24" aria-hidden="true"><path d="M2 5h20v14H2z M3.5 6.5 12 13l8.5-6.5" fill="var(--navy)" stroke="#fff" stroke-width="1.6"/></svg></p>
      <p class="line">www.wardcompass-example.com
        <svg viewBox="0 0 24 24" aria-hidden="true"><circle cx="12" cy="12" r="10"/><path d="M2 12h20M12 2c3 3 3 17 0 20M12 2c-3 3-3 17 0 20" stroke="#fff" stroke-width="1.4" fill="none"/></svg></p>
      <p class="line address">14 Annakhil 3 H.R.B. Rabat, Morocco</p>
    </div>
  </section>
</main>
</body>
</html>
```